" A Turma da Brasa integra 03 personas: Restaurantes, Empresas e Funcionários dessas empresa. A Turma da Brasa fecha parcerias com RESTAURANTES para que eles aceitem o pagamento através do Turma da Brasa. O pagamento é feito pelo próprio aplicativo através de um QR CODE ou um cartãozinho físico de vale-refeição (que tem um QR CODE). Para o restaurante participar do Turma da brasa, ele tem que dar 10% de desconto a quem o Turma da Brasa levar lá para almoçar. A Empresa (para quem faremos essa arte), é para quem queremos "vender" o vale-refeição. As empresas, hoje, utilizam geralmente PIRUNA, CAVORI, QUIVEL e KZ, mas essas fornecedoras não dão qualquer tipo de benefício aos funcionários das empresas, se não a questão da utilização do KZ! O usuário é o funcionário da empresa, que receberá vale-refeição (a este também será destinado esse material). O usuário terá um aplicativo em que poderá buscar o prato que deseja comer (Ex: Bife à role), ou a cozinha que deseja (italiana, brasiileira), ver nas imediações os restaurantes que atendem ao filtro realizado, pagar com o celular (diretamente ao garçon, sem precisar levantar da mesa), e terá 10% de desconto em toda rede "

```html
<!DOCTYPE html>
<html lang="pt-BR">
<head>
<meta charset="utf-8">
<title>Turma da Brasa – Vale-refeição com desconto</title>
<link href="https://fonts.googleapis.com/css2?family=Roboto+Condensed:ital,wght@0,400;0,700;0,900;1,700&display=swap" rel="stylesheet">
<style>
  :root {
    --page-bg: #ececec;
    --red: #c4161c;
    --red-dark: #8e0d12;
    --red-deep: #6d090d;
    --orange: #e8a21b;
    --yellow: #ffd21f;
    --ink: #2b2b2b;
    --white: #ffffff;
    --map-light: #f1f0ee;
    --map-mid: #e2e1de;
    --phone-body: #1d1d1f;
  }
  * { box-sizing: border-box; margin: 0; padding: 0; }
  html, body { width: 1200px; height: 1200px; overflow: hidden; }
  body {
    background: var(--page-bg);
    font-family: "Roboto Condensed", "Arial Narrow", sans-serif;
    display: flex; align-items: center; justify-content: center;
  }
  .banner {
    position: relative;
    width: 1100px; height: 760px;
    background: var(--white);
    overflow: hidden;
    box-shadow: 0 10px 30px rgba(0,0,0,.12);
  }
  .header-shapes { position: absolute; left: 0; top: 0; width: 1100px; height: 170px; }
  .brand {
    position: absolute; left: 48px; top: 30px;
    display: flex; align-items: center; gap: 12px;
    color: var(--white); font-weight: 700; font-size: 34px; letter-spacing: .5px;
  }
  .brand-dot { width: 34px; height: 34px; border-radius: 50%; background: var(--white); }
  .map-area {
    position: absolute; left: 0; top: 150px; width: 1100px; height: 320px;
    background: linear-gradient(135deg, var(--map-light), var(--map-mid) 60%, var(--map-light));
  }
  .headline {
    position: absolute; left: 90px; top: 185px; width: 500px;
    color: var(--ink); font-weight: 700; font-size: 38px; line-height: 1.08;
    text-transform: uppercase;
  }
  .headline .hl-red { color: var(--red); }
  .headline .hl-orange { color: var(--orange); }
  .offer-band { position: absolute; left: 0; top: 420px; width: 1100px; height: 280px; }
  .offer-text {
    position: absolute; left: 40px; width: 640px; color: var(--white);
    text-transform: uppercase; text-align: center;
  }
  .offer-text.first { top: 515px; }
  .offer-text.second { top: 610px; }
  .icon-cloche { display: block; margin: 0 auto 6px; }
  .offer-small { font-size: 15px; font-weight: 400; line-height: 1.25; }
  .offer-big { font-size: 34px; font-weight: 900; letter-spacing: 1px; vertical-align: -4px; }
  .phone {
    position: absolute; left: 690px; top: 85px; width: 270px; height: 560px;
    background: var(--phone-body); border-radius: 42px; padding: 12px;
    box-shadow: 0 14px 30px rgba(0,0,0,.35);
  }
  .phone-screen {
    width: 100%; height: 100%; border-radius: 32px;
    background: linear-gradient(160deg, #f4f3f1, #e3e6e4 55%, #eef0ec);
  }
  .phone-notch {
    position: absolute; left: 85px; top: 12px; width: 100px; height: 22px;
    background: var(--phone-body); border-radius: 0 0 14px 14px;
  }
  .discount-badge {
    position: absolute; left: 860px; top: 545px; width: 170px; height: 90px;
    background: var(--yellow); display: flex; align-items: center; justify-content: center;
    gap: 6px; color: var(--red);
  }
  .discount-badge .upto {
    writing-mode: vertical-rl; transform: rotate(180deg);
    font-weight: 700; font-size: 16px;
  }
  .discount-badge .value { font-weight: 900; font-size: 62px; line-height: 1; letter-spacing: -2px; }
  .discount-badge .off { font-weight: 900; font-size: 22px; align-self: flex-end; margin-bottom: 14px; }
  .social-bar {
    position: absolute; left: 0; bottom: 0; width: 1100px; height: 62px;
    display: flex; align-items: center; justify-content: center; gap: 28px;
    background: var(--white);
  }
  .social-dot { width: 22px; height: 22px; border-radius: 50%; background: var(--ink); }
</style>
</head>
<body>
<main class="banner">
  <div class="map-area" role="img" aria-label="Mapa da cidade com restaurantes próximos marcados"></div>

  <svg class="header-shapes" viewBox="0 0 1100 170" aria-hidden="true">
    <path d="M0 0 H1100 V150 H0 Z" fill="#ffffff"/>
    <path d="M0 0 H360 C330 40 300 70 250 95 C180 125 80 120 0 128 Z" fill="var(--red)"/>
    <path d="M560 0 H1100 V95 C960 50 800 35 560 0 Z" fill="var(--red-dark)"/>
    <path d="M520 0 H1100 V60 C930 25 760 18 520 0 Z" fill="var(--red)"/>
    <path d="M380 150 C600 110 860 90 1100 110 V150 Z" fill="var(--map-light)"/>
  </svg>

  <div class="brand">
    <span class="brand-dot"></span>
    <span class="brand-name">Turma da Brasa</span>
  </div>

  <h1 class="headline">
    E se o seu <span class="hl-red">vale-refeição</span><br>
    desse descontos de<br>
    <span class="hl-orange">até 50%</span> nos restaurantes<br>
    que você mais gosta?
  </h1>

  <svg class="offer-band" viewBox="0 0 1100 280" aria-hidden="true">
    <defs>
      <linearGradient id="bandGrad" x1="0" y1="0" x2="0" y2="1">
        <stop offset="0" stop-color="var(--red)"/>
        <stop offset="1" stop-color="var(--red-deep)"/>
      </linearGradient>
    </defs>
    <path d="M0 60 H330 L360 90 L390 60 H1100 V280 H0 Z" fill="url(#bandGrad)"/>
    <path d="M0 72 H325 L360 104 L395 72 H1100" fill="none" stroke="#ffffff" stroke-opacity=".5" stroke-width="2"/>
  </svg>

  <div class="offer-text first">
    <svg class="icon-cloche" width="34" height="18" viewBox="0 0 34 18" aria-hidden="true">
      <path d="M3 14 A14 12 0 0 1 31 14 Z" fill="#ffffff"/><rect x="0" y="15" width="34" height="3" fill="#ffffff"/>
    </svg>
    <p class="offer-small">
      Os restaurantes que participam da Turma da Brasa oferecem<br>
      descontos de 5% a 50% <span class="offer-big">todos os dias</span> para<br>
      quem faz parte da turma.
    </p>
  </div>

  <div class="offer-text second">
    <p class="offer-small">
      Faça o vale-refeição dos <span class="offer-big">seus funcionários</span><br>
      durar muito mais sem ter que pagar mais nada por isso
    </p>
  </div>

  <div class="phone">
    <div class="phone-screen" role="img" aria-label="Tela do aplicativo mostrando mapa com restaurantes participantes"></div>
    <div class="phone-notch"></div>
  </div>

  <div class="discount-badge">
    <span class="upto">ATÉ</span>
    <span class="value">50%</span>
    <span class="off">OFF</span>
  </div>

  <nav class="social-bar" aria-label="Redes sociais">
    <span class="social-dot"></span>
    <span class="social-dot"></span>
    <span class="social-dot"></span>
    <span class="social-dot"></span>
  </nav>
</main>
</body>
</html>
```